Basic Website Design for Healthcare Services Startup

We need a professional designer to take our existing basic mobile website and create professional mobile and desktop website designs. We need the designer to use the existing content and page structure at our current mobile website (http://www.vantrilo.com/phone/index.html) for the new design. Let us know if you have suggestions on how we can improve the site map.

The design needs to feel contemporary and clean. We need to convey a very professional operation that embraces technology. PLEASE refer to the attached brochure to understand the style and feel we want the website to have.

We want to start small and quickly iterate to a larger, final product. Initial submissions should only include a desktop homepage and a mobile homepage. I WILL PROVIDE INITIAL FEEDBACK AND COMMIT MONEY TO THE PROJECT BEFORE ASKING DESIGNERS TO COMPLETE A FULL DESIGN FOR THE ENTIRE DESKTOP AND MOBILE SITE.

We are happy to email you any stock photos you see on our current site. Please feel free to ask questions.

Please stay close to our current color scheme, but feel free to add new colors to our palette as needed.
Our blue is: #7CD9DA
Our gray is: #585751

Thanks Designers!!

Target Market(s)

Males, Ages 18-24

Industry/Entity Type

Health Care

Number of Pages Required

5+ page

Font styles to use
Sans Serif

Requirements
Must have
• -Final design must contain all content on www.vantrilo.com/phone/ website.
• -All graphics/designs/content must be easily accessible in the final deliverable so we can import it into Adobe Muse for development.
• -Must be designed in Adobe.
• -Please specify different states: normal, rollover, active, etc.
• ***UPDATE***
• Thank you everyone for your submissions! I am very happy with the quality of submissions so I will commit to the guarantee. Please focus on my comments and submit your best 2 or 3 designers. I want to give strong feedback to all designers and it is difficult when there are many different combinations of the same design elements.
• A few quick notes to help guide future submissions:
• 1.) PICTURE CONTENT: right now the focus is on designing the landing page for our donors, so the audience is 18-24 males. We want a few medical pictures, but we mostly want to connect with our donor base. Please save the pictures of doctors for the HOSPITAL PAGE. For this main page we either want to see black or hispanic people donating blood, having fun, or being with friends and loved ones.
• 2.) HOMEPAGE CONTENT: Please use the content on www.vantrilo.com/phone/index.html for homepage content guidance. We do not want to include a lot of the hospital brochure content on the homepage we want that content on the HOSPITAL PAGE).
• 3.) BLOG CONTENT: Add a section for articles/blog content. We want to feature the most recent post and small previews of the previous 2 or 3 articles.
• 4.) SOCIAL: we want our social media icons to be prominent. Either in the header or at the top of the page.
• 5.) NO PARTNERS: we don't want to include our partners on the donor homepage.
• ***UPDATE***
• Hi everyone, quick clarification. The final winner will need to include all these pages. Most of them should be very quick because they do not have a lot of content on them. Please focus on the donor homepage. I will approve the look and feel before asking you to create the rest of the pages. Please note I need both Desktop and
• Mobile versions of these designs:
• Pages Needed in final design:
• -Homepage <= 85% of design work should be on this page
• -Registration
• -Hospital
• -Donor Eligibility
• -How Vantrilo Works
• -Learn About PBSC Donation
• -Learn About Blood Cancer
• -About Us
Nice to have
• -Nice to have an idea how we can make your design responsive.
Should not have
• None.

```html
<!DOCTYPE html>
<html lang="en">
<head>
<meta charset="utf-8">
<title>Vantrilo — Earn Money While You Save a Life</title>
<link href="https://fonts.googleapis.com/css2?family=Raleway:wght@300;400;500;600;700&family=Open+Sans:ital,wght@0,400;0,600;1,400&display=swap" rel="stylesheet">
<style>
  :root{
    --teal:#7CD9DA;
    --teal-deep:#5bc2c3;
    --teal-overlay:rgba(124,217,218,.55);
    --gray:#585751;
    --gray-dark:#4a4944;
    --ink:#3a3a36;
    --paper:#ffffff;
  }
  *{box-sizing:border-box;margin:0;padding:0}
  html,body{width:1200px;height:2260px;overflow:hidden}
  body{font-family:"Open Sans",Arial,sans-serif;color:var(--ink);background:var(--paper)}
  a{text-decoration:none}
  .page{position:relative;width:1200px;height:2260px}

  /* header */
  .site-header{height:112px;position:relative;background:var(--paper)}
  .brand{position:absolute;left:40px;top:26px}
  .brand-name{font-family:"Open Sans",sans-serif;font-weight:600;font-size:30px;letter-spacing:2px;color:var(--teal-deep);text-transform:uppercase}
  .social{position:absolute;right:40px;top:18px;display:flex;gap:8px}
  .social span{width:28px;height:28px;background:var(--teal);border-radius:3px;display:block}
  .main-nav{position:absolute;right:40px;top:62px;display:flex}
  .main-nav a{font-family:"Raleway",sans-serif;font-size:15px;font-weight:600;color:var(--gray);text-transform:uppercase;padding:12px 15px;letter-spacing:.5px}
  .main-nav a.active{background:var(--teal);color:#fff}

  /* hero */
  .hero{position:relative;height:500px;overflow:hidden}
  .hero-photo{position:absolute;inset:0;background:linear-gradient(120deg,#5e6a6c 0%,#8fa3a6 40%,#6f8587 70%,#4d5a5c 100%)}
  .hero-tint{position:absolute;inset:0;background:var(--teal-overlay)}
  .hero-content{position:relative;text-align:center;padding-top:190px;color:#fff}
  .hero-title{font-family:"Raleway",sans-serif;font-weight:400;font-size:50px;letter-spacing:2px;text-transform:uppercase}
  .hero-sub{font-size:22px;margin-top:8px}
  .btn-outline{display:inline-block;margin-top:28px;border:2px solid #fff;border-radius:30px;padding:12px 36px;color:#fff;font-family:"Raleway",sans-serif;font-weight:600;font-size:18px;text-transform:uppercase;letter-spacing:1px}
  .hero-arrow{position:absolute;top:232px;width:36px;height:36px;border-radius:50%;background:rgba(255,255,255,.35)}
  .hero-arrow.prev{left:40px}.hero-arrow.next{right:40px}
  .hero-arrow svg{position:absolute;left:10px;top:10px}

  /* need section */
  .need{position:relative;height:520px;background:var(--teal);color:#fff;padding:40px 60px}
  .need-title{font-family:"Raleway",sans-serif;font-weight:500;font-size:34px;text-transform:uppercase;letter-spacing:1px}
  .need-rule{height:2px;background:rgba(255,255,255,.7);margin:14px 0 26px}
  .need-list{list-style:none;width:560px}
  .need-list li{position:relative;padding-left:34px;font-size:17px;line-height:1.5;margin-bottom:14px}
  .need-list svg{position:absolute;left:0;top:6px}
  .btn-light{display:inline-block;margin-top:6px;border:2px solid #fff;border-radius:4px;padding:9px 26px;color:#fff;font-weight:600;font-size:16px}
  .video{position:absolute;right:32px;top:132px;width:448px;height:256px;background:linear-gradient(135deg,#6d6a63,#3c3b37)}
  .video-play{position:absolute;left:189px;top:93px;width:70px;height:70px;border-radius:50%;background:rgba(255,255,255,.85)}
  .video-play svg{position:absolute;left:26px;top:20px}
  .video-bar{position:absolute;left:0;right:0;bottom:0;height:26px;background:rgba(0,0,0,.5)}

  /* testimonials */
  .testimonials{height:300px;background:var(--gray);color:#fff;padding:28px 60px;position:relative}
  .section-title{font-family:"Raleway",sans-serif;font-weight:500;font-size:34px;text-transform:uppercase;letter-spacing:1px}
  .testimonials .section-title{color:#e8e8e4}
  .testimonials .rule{height:2px;background:rgba(255,255,255,.4);margin:14px 0 0}
  .quote-badge{position:absolute;left:60px;top:136px;width:58px;height:58px;background:var(--teal);border-radius:4px}
  .quote-badge span{position:absolute;left:14px;top:-4px;font-family:Georgia,serif;font-size:60px;color:#fff}
  .avatar{position:absolute;left:160px;top:112px;width:130px;height:130px;border-radius:50%;background:linear-gradient(160deg,#c9b7a6,#7c6a5c);border:4px solid #fff}
  .quote{position:absolute;left:340px;top:140px;width:800px;font-style:italic;font-size:16px;line-height:1.65;color:#f0f0ec}
  .quote-author{position:absolute;left:340px;top:218px;font-size:15px;color:#ddd}
  .dots{position:absolute;right:60px;top:236px;display:flex;gap:8px}
  .dots span{width:14px;height:14px;border-radius:50%;background:#8e8d87}
  .dots span.on{background:var(--teal)}

  /* blog */
  .blog{height:388px;padding:26px 60px 0}
  .title-lead{color:var(--gray)}
  .title-accent{color:var(--teal-deep)}
  .blog .rule,.involved .rule{height:2px;background:#ddd;margin:12px 0 22px}
  .posts{display:flex;gap:40px}
  .post{width:333px}
  .post-photo{height:164px}
  .post-meta{display:flex;gap:16px;margin-top:14px}
  .post-date{width:56px;border:2px solid var(--teal);text-align:center;flex:none}
  .post-date b{display:block;font-size:24px;color:var(--teal-deep);line-height:1.3}
  .post-date i{display:block;font-style:normal;font-size:12px;background:var(--teal);color:#fff;text-transform:uppercase}
  .post-text{font-size:15px;line-height:1.5;color:var(--teal-deep)}

  /* get involved */
  .involved{height:208px;padding:18px 60px 0}
  .involved .rule{margin-bottom:28px}
  .cta-row{display:flex;gap:60px}
  .cta{width:510px;height:64px;border-radius:34px;display:flex;align-items:center;font-family:"Raleway",sans-serif;font-weight:600;font-size:22px;text-transform:uppercase;letter-spacing:1px}
  .cta-icon{width:64px;height:64px;border-radius:50%;display:flex;align-items:center;justify-content:center;margin-right:90px}
  .cta.hero-cta{background:var(--teal);color:#fff;border:3px solid var(--teal)}
  .cta.hero-cta .cta-icon{background:#fff;border:3px solid var(--teal);margin-left:-3px}
  .cta.drive{border:3px solid var(--gray);color:var(--gray)}
  .cta.drive .cta-icon{background:var(--gray);margin-left:-3px}

  /* footer */
  .site-footer{height:232px;background:var(--gray-dark);color:#ddd;padding:22px 60px;position:relative}
  .footer-links{text-align:center;font-size:13px}
  .footer-links a{color:#ddd;margin:0 6px}
  .footer-links a.active{color:var(--teal)}
  .contacts{display:flex;justify-content:space-between;margin-top:34px;padding:0 80px}
  .contact{display:flex;gap:12px;align-items:flex-start}
  .contact-icon{width:40px;height:40px;background:var(--teal);border-radius:3px;display:flex;align-items:center;justify-content:center}
  .contact b{display:block;font-size:13px;color:var(--teal);text-transform:uppercase}
  .contact span{font-size:13px}
  .footer-base{position:absolute;left:60px;right:60px;bottom:20px;display:flex;justify-content:space-between;align-items:center;font-size:12px;color:#aaa}
  .footer-base .social{position:static;gap:6px}
  .footer-base .social span{width:22px;height:22px}
</style>
</head>
<body>
<div class="page">

  <header class="site-header">
    <div class="brand"><span class="brand-name">Vantrilo</span></div>
    <div class="social"><span></span><span></span><span></span></div>
    <nav class="main-nav">
      <a href="#" class="active">Home</a>
      <a href="#">About Us</a>
      <a href="#">Get Involved</a>
      <a href="#">Why Sign Up?</a>
      <a href="#">How Vantrilo Works</a>
      <a href="#">Donor Eligibility</a>
      <a href="#">Contact Us</a>
    </nav>
  </header>

  <section class="hero">
    <div class="hero-photo" role="img" aria-label="Donor resting in a clinic chair during a blood stem cell donation"></div>
    <div class="hero-tint"></div>
    <span class="hero-arrow prev"><svg width="16" height="16" viewBox="0 0 16 16"><path d="M11 2 L5 8 L11 14" stroke="#fff" stroke-width="2.5" fill="none"/></svg></span>
    <span class="hero-arrow next"><svg width="16" height="16" viewBox="0 0 16 16"><path d="M5 2 L11 8 L5 14" stroke="#fff" stroke-width="2.5" fill="none"/></svg></span>
    <div class="hero-content">
      <h1 class="hero-title">Earn Money While You Save a Life</h1>
      <p class="hero-sub">Donors will receive $2,000 for each donation</p>
      <a class="btn-outline" href="#">Register Today</a>
    </div>
  </section>

  <section class="need">
    <h2 class="need-title">You Are Desperately Needed to Save a Life</h2>
    <div class="need-rule"></div>
    <ul class="need-list">
      <li><svg width="18" height="14" viewBox="0 0 18 14"><path d="M1 7 L6 12 L17 1" stroke="#fff" stroke-width="2.5" fill="none"/></svg>1 in 3 minority blood cancer patients cannot find a donor</li>
      <li><svg width="18" height="14" viewBox="0 0 18 14"><path d="M1 7 L6 12 L17 1" stroke="#fff" stroke-width="2.5" fill="none"/></svg>You might be the ONLY person that can save someone's life</li>
      <li><svg width="18" height="14" viewBox="0 0 18 14"><path d="M1 7 L6 12 L17 1" stroke="#fff" stroke-width="2.5" fill="none"/></svg>Matches usually occur between people of the same race</li>
      <li><svg width="18" height="14" viewBox="0 0 18 14"><path d="M1 7 L6 12 L17 1" stroke="#fff" stroke-width="2.5" fill="none"/></svg>Over 8,000 Americans need a blood stem cell donation each year</li>
      <li><svg width="18" height="14" viewBox="0 0 18 14"><path d="M1 7 L6 12 L17 1" stroke="#fff" stroke-width="2.5" fill="none"/></svg>Vantrilo recruits donors for African American, Asian, and Hispanic communities</li>
    </ul>
    <a class="btn-light" href="#">Register Today</a>
    <div class="video" role="img" aria-label="Video still of a donor speaking about his experience">
      <span class="video-play"><svg width="24" height="30" viewBox="0 0 24 30"><path d="M0 0 L24 15 L0 30 Z" fill="#4a4944"/></svg></span>
      <span class="video-bar"></span>
    </div>
  </section>

  <section class="testimonials">
    <h2 class="section-title">Testimonials</h2>
    <div class="rule"></div>
    <span class="quote-badge"><span>&ldquo;</span></span>
    <div class="avatar" role="img" aria-label="Portrait of a donor"></div>
    <p class="quote">&ldquo;Matching as a donor has been an honor and a privilege. There are no words to describe the miraculous feeling that comes with having the ability to provide someone with the opportunity for a second chance at life.&rdquo;</p>
    <p class="quote-author">- Jenna</p>
    <div class="dots"><span class="on"></span><span></span><span></span></div>
  </section>

  <section class="blog">
    <h2 class="section-title"><span class="title-lead">Latest</span> <span class="title-accent">Blog</span></h2>
    <div class="rule"></div>
    <div class="posts">
      <article class="post">
        <div class="post-photo" role="img" aria-label="Medical team smiling together" style="background:linear-gradient(135deg,#b9d8e6,#4e8fa8)"></div>
        <div class="post-meta"><div class="post-date"><b>26</b><i>Feb</i></div><p class="post-text">Lorem ipsum dolor sit amet cons ctur adipiscing elit</p></div>
      </article>
      <article class="post">
        <div class="post-photo" role="img" aria-label="Group of friends in black and white" style="background:linear-gradient(135deg,#e2e2e2,#8a8a8a)"></div>
        <div class="post-meta"><div class="post-date"><b>30</b><i>Feb</i></div><p class="post-text">Lorem ipsum dolor sit amet cons ctur adipiscing elit</p></div>
      </article>
      <article class="post">
        <div class="post-photo" role="img" aria-label="Smiling family together outdoors" style="background:linear-gradient(135deg,#e8cdb6,#a97b5a)"></div>
        <div class="post-meta"><div class="post-date"><b>02</b><i>Mar</i></div><p class="post-text">Lorem ipsum dolor sit amet cons ctur adipiscing elit</p></div>
      </article>
    </div>
  </section>

  <section class="involved">
    <h2 class="section-title"><span class="title-lead">Get</span> <span class="title-accent">Involved</span></h2>
    <div class="rule"></div>
    <div class="cta-row">
      <a class="cta hero-cta" href="#"><span class="cta-icon"><svg width="28" height="24" viewBox="0 0 28 24"><path d="M14 23 L3 12 A6.5 6.5 0 0 1 14 4 A6.5 6.5 0 0 1 25 12 Z" fill="#7CD9DA"/></svg></span>Become a H.E.R.O</a>
      <a class="cta drive" href="#"><span class="cta-icon"><svg width="26" height="26" viewBox="0 0 26 26"><rect x="3" y="3" width="20" height="20" rx="2" fill="none" stroke="#fff" stroke-width="2.5"/><path d="M8 13 H18 M13 8 V18" stroke="#fff" stroke-width="2.5"/></svg></span>Organize a Donor Drive</a>
    </div>
  </section>

  <footer class="site-footer">
    <nav class="footer-links">
      <a href="#" class="active">Home</a>| <a href="#">About Us</a>| <a href="#">Get Involved</a>| <a href="#">How Vantrilo Works</a>| <a href="#">Donor Eligibility</a>| <a href="#">Contact Us</a>| <a href="#">Terms of Use</a>| <a href="#">Legal and Privacy Policy</a>
    </nav>
    <div class="contacts">
      <div class="contact"><span class="contact-icon"><svg width="16" height="20" viewBox="0 0 16 20"><path d="M8 19 C3 12 1 9 1 7 A7 7 0 0 1 15 7 C15 9 13 12 8 19 Z" fill="#fff"/><circle cx="8" cy="7" r="2.5" fill="#7CD9DA"/></svg></span><div><b>Address</b><span>4820 Larkin Avenue, Suite 3 | Eastford, MD 20117</span></div></div>
      <div class="contact"><span class="contact-icon"><svg width="18" height="18" viewBox="0 0 18 18"><path d="M4 1 L7 5 L5 7 C6 10 8 12 11 13 L13 11 L17 14 L15 17 C8 17 1 10 1 3 Z" fill="#fff"/></svg></span><div><b>Phone</b><span>(202) 555-0147</span></div></div>
      <div class="contact"><span class="contact-icon"><svg width="20" height="14" viewBox="0 0 20 14"><rect x="1" y="1" width="18" height="12" fill="none" stroke="#fff" stroke-width="2"/><path d="M1 1 L10 8 L19 1" stroke="#fff" stroke-width="2" fill="none"/></svg></span><div><b>Email</b><span>info@vantrilo.com</span></div></div>
    </div>
    <div class="footer-base">
      <span>Copyright &copy; 2015 Vantrilo. All Rights Reserved.</span>
      <div class="social"><span></span><span></span><span></span></div>
    </div>
  </footer>

</div>
</body>
</html>
```